CANNABIS GROWING MACHINES Business Card Design

I created a front and back idea of what I want. Also I included my Brightleaf Plot logo to be used on the card. Please use your creativity to make it look professional and awesome! Use the all text and phrases in the sample card that I made.

(Front of card)Key words and phrases:
CANNABIS GROWING MACHINES
Aeroponics Technology
No soil
No pesticides
98% less water
Grow year round

(Back of card)
EVERY MONTH ONE SPIRE PLANTER WILL BE GIVEN AWAY
FOLLOW US ON IG FOR A CHANCE TO WIN A SPIRE PLANTER
CANNABIS GROWING MACHINES
Vertical Farming
Urban Farming
100% Organic
Grows 40% Faster
Indoors/outdoors

My contact info:
Chef Rom
Phone:555 014-3397
web: brightleafplot.example
IG: mossyfingerscrew

Target Market(s)

Cannabis Cultivation, Gardening, Urban farming, Vertical farming

Industry/Entity Type

Cannabis

Contact Information for Business Card

My contact info:
Chef Rom
Phone:555 014-3397
web: brightleafplot.example
IG: mossyfingerscrew

Requirements
Must have
• My contact info:
Chef Rom
Phone:555 014-3397
web: brightleafplot.example
IG: mossyfingerscrew
Nice to have
• Awesome Cannabis imagery throughout the card front and back.

```html
<!DOCTYPE html>
<html lang="en">
<head>
<meta charset="utf-8">
<title>Brightleaf Plot — Business Card</title>
<link href="https://fonts.googleapis.com/css2?family=Open+Sans:wght@400;600;700&display=swap" rel="stylesheet">
<style>
  :root {
    --bg: #2b2b2b;
    --card: #f7f7f7;
    --green: #7cb342;
    --olive: #5f7f2a;
    --ink: #3a3a3a;
    --rule: #555555;
    --leaf-dark: #3f6b2a;
    --leaf-light: #9cc46a;
  }
  * { box-sizing: border-box; margin: 0; padding: 0; }
  html, body { width: 1200px; height: 900px; overflow: hidden; }
  body {
    background: var(--bg);
    font-family: "Open Sans", Arial, sans-serif;
    position: relative;
  }
  .card {
    position: absolute;
    left: 250px;
    width: 700px;
    height: 400px;
    background: linear-gradient(135deg, #ffffff 0%, var(--card) 60%, #ececec 100%);
    overflow: hidden;
  }
  .card--back { top: 40px; }
  .card--front { top: 460px; }

  .brand {
    display: flex;
    align-items: center;
    gap: 12px;
    color: var(--ink);
    font-weight: 600;
    letter-spacing: 6px;
    line-height: 1.05;
    font-size: 22px;
  }
  .brand__dot {
    width: 34px; height: 34px;
    border-radius: 50%;
    background: var(--green);
    flex: none;
  }

  /* back: contact side */
  .card--back .brand { position: absolute; left: 50px; top: 70px; }
  .divider {
    position: absolute; left: 300px; top: 40px;
    width: 1.5px; height: 120px; background: var(--rule);
  }
  .contact { position: absolute; left: 325px; top: 36px; color: var(--ink); }
  .contact__name {
    color: var(--green); font-weight: 700; font-size: 22px; letter-spacing: 0.5px;
    margin-bottom: 6px;
  }
  .contact__row { display: flex; align-items: center; gap: 8px; font-size: 17px; line-height: 27px; }
  .contact__row svg { width: 15px; height: 15px; flex: none; }
  .promo {
    position: absolute; left: 0; right: 0; top: 205px;
    text-align: center; color: var(--green);
    font-size: 17px; line-height: 25px;
  }
  .features {
    position: absolute; left: 0; right: 0; top: 300px;
    text-align: center; color: var(--green);
    font-weight: 700; font-size: 19px; line-height: 28px;
  }

  /* front: product side */
  .card--front .brand { position: absolute; left: 40px; top: 44px; font-size: 24px; }
  .photos { position: absolute; inset: 0; width: 700px; height: 400px; }
  .pitch { position: absolute; left: 40px; top: 170px; color: var(--green); font-weight: 700; }
  .pitch__title { font-size: 24px; line-height: 30px; }
  .pitch__sub { font-size: 22px; line-height: 30px; }
  .benefits { position: absolute; left: 44px; top: 250px; list-style: none; color: var(--ink); }
  .benefits li { display: flex; align-items: center; gap: 10px; font-size: 20px; line-height: 33px; }
  .benefits li::before {
    content: ""; width: 10px; height: 10px; border-radius: 50%; background: var(--green); flex: none;
  }
</style>
</head>
<body>

<section class="card card--back">
  <div class="brand"><span class="brand__dot"></span><span>BRIGHTLEAF<br>PLOT</span></div>
  <div class="divider"></div>
  <div class="contact">
    <div class="contact__name">CHEF ROM</div>
    <div class="contact__row">
      <svg viewBox="0 0 16 16" aria-hidden="true"><path fill="#7cb342" d="M3 1h3l1.5 4-2 1.2a9 9 0 0 0 4.3 4.3L11 8.5l4 1.5v3a2 2 0 0 1-2 2A12 12 0 0 1 1 3a2 2 0 0 1 2-2z"/></svg>
      <span>555 014-3397</span>
    </div>
    <div class="contact__row">
      <svg viewBox="0 0 16 16" aria-hidden="true"><circle cx="8" cy="8" r="6.5" fill="none" stroke="#7cb342" stroke-width="1.6"/><path d="M1.5 8h13M8 1.5c-3 3.5-3 9.5 0 13M8 1.5c3 3.5 3 9.5 0 13" fill="none" stroke="#7cb342" stroke-width="1.2"/></svg>
      <span>brightleafplot.example</span>
    </div>
    <div class="contact__row">
      <svg viewBox="0 0 16 16" aria-hidden="true"><rect x="1" y="1" width="14" height="14" rx="3" fill="#7cb342"/></svg>
      <span>mossyfingerscrew</span>
    </div>
  </div>
  <p class="promo">
    Every Month One Spire Planter Will Be Given Away<br>
    Follow Us On Ig For A Chance To Win A Spire Planter<br>
    Cannabis Growing Machines
  </p>
  <p class="features">
    Vertical Farming / Urban Farming / 100% Organic<br>
    Grows 40% Faster / Indoors / outdoors
  </p>
</section>

<section class="card card--front">
  <svg class="photos" viewBox="0 0 700 400">
    <defs>
      <linearGradient id="budTop" x1="0" y1="0" x2="1" y2="1">
        <stop offset="0" stop-color="#a8c98a"/>
        <stop offset="0.5" stop-color="#4f7a3a"/>
        <stop offset="1" stop-color="#2f5a2a"/>
      </linearGradient>
      <linearGradient id="budBottom" x1="0" y1="0" x2="1" y2="1">
        <stop offset="0" stop-color="#dfe8d0"/>
        <stop offset="0.5" stop-color="#8cb55a"/>
        <stop offset="1" stop-color="#5e8f34"/>
      </linearGradient>
    </defs>
    <polygon points="352,112 468,-4 704,-4 704,244" fill="var(--olive)"/>
    <polygon role="img" aria-label="Close-up photo of a frosty cannabis bud in an indoor grow" points="364,112 472,4 700,4 700,66 478,150" fill="url(#budTop)"/>
    <polygon role="img" aria-label="Photo of flowering cannabis plants growing in a planter" points="486,160 700,78 700,236" fill="url(#budBottom)"/>
  </svg>
  <div class="brand"><span class="brand__dot"></span><span>BRIGHTLEAF<br>PLOT</span></div>
  <div class="pitch">
    <div class="pitch__title">CANNABIS GROWING MACHINES</div>
    <div class="pitch__sub">Aeroponics Technology</div>
  </div>
  <ul class="benefits">
    <li>No soil</li>
    <li>No pesticides</li>
    <li>98% less water</li>
    <li>Grow year round</li>
  </ul>
</section>

</body>
</html>
```